A new company focused on starting and investing in transformative businesses.

We need a simple and clean website with a few pages. we like larkmeadow.com as a starting point. we want the landing page to be very simple with an option to click through on the top right into INVESTOR LOGIN. then we want to be able to scroll down to see more about our company.

Target Market(s)

professional

Coding

Coded - Design and coding required

Number of Pages Required

2 page

Font styles to use
Serif
Sans Serif

Requirements
Must have
• HALVERN BUILDERS logo (attached as a file) on the top with INVESTOR LOGIN as a click through on the right. Please model the click through from larkmeadow.com. The description (also written in attached file) should be on the landing page. we do not want to have to scroll to read the description.

Then we can scroll down to read more about Halvern including the mission and the two types of businesses. More is detailed on the attached file called "Halvern Website Syntax"
Should not have
• should not be slow loading with lots of fancy graphics. should not be busy and with too many colors.

```html
<!DOCTYPE html>
<html lang="en">
<head>
<meta charset="utf-8">
<title>Halvern Builders</title>
<link href="https://fonts.googleapis.com/css2?family=Nunito+Sans:wght@400;600;700;800&display=swap" rel="stylesheet">
<style>
:root{
  --brand:#0b58a6;
  --brand-bright:#0d66b5;
  --brand-deep:#0e5aa7;
  --ink:#1d1d1f;
  --text:#3c3c40;
  --muted:#5b5b60;
  --mist:#eef0f4;
  --white:#ffffff;
  --night:#231f20;
  --field:#ffffff;
}
*{box-sizing:border-box;margin:0;padding:0}
html,body{width:1200px;height:3938px;overflow:hidden}
body{position:relative;font-family:"Nunito Sans",Arial,sans-serif;color:var(--text);background:var(--white)}
.abs{position:absolute}
a{color:inherit;text-decoration:none}

/* brand lockup */
.brand{position:absolute;display:flex;align-items:center;gap:14px;font-weight:800;letter-spacing:1px}
.brand-mark{flex:none;border-radius:3px}
.brand-name{display:block;line-height:1.1;white-space:nowrap}

/* header */
.site-header{position:absolute;left:0;top:0;width:1200px;height:102px;background:var(--white)}
.header-brand{left:66px;top:20px;font-size:26px;color:var(--brand)}
.header-brand .brand-mark{width:48px;height:60px;background:var(--brand)}
.main-nav{position:absolute;top:38px;font-size:16px;color:var(--ink)}
.main-nav a{position:absolute;white-space:nowrap}
.main-nav .current{color:var(--brand);font-weight:700;text-decoration:underline}
.btn{position:absolute;display:flex;align-items:center;justify-content:center;gap:8px;background:var(--brand);color:var(--white);font-weight:700;border-radius:2px}
.investor-login{left:981px;top:29px;width:158px;height:41px;font-size:16px}

/* hero */
.hero{position:absolute;left:0;top:102px;width:1200px;height:633px;
  background:linear-gradient(180deg,#3f86c4 0%,#5c9fd3 22%,#1e6aa6 45%,#0d4f84 70%,#0a3a63 100%)}
.hero-title{left:203px;top:292px;font-size:55px;font-weight:700;color:var(--white);letter-spacing:-0.5px}
.hero-lede{left:203px;top:362px;font-size:25px;line-height:35px;color:var(--white)}
.get-started{left:203px;top:466px;width:188px;height:49px;font-size:17px;letter-spacing:.5px}
.round-arrow{position:absolute;width:52px;height:52px}

/* mission intro */
.mission-visual{left:188px;top:848px;width:237px;height:299px;border-radius:4px;
  background:linear-gradient(135deg,#c9d8ea,#8aa6c6 55%,#3d6da3)}
.mission-heading{left:546px;top:846px;width:500px;font-size:24px;line-height:32px;font-weight:800;color:var(--ink)}
.mission-copy{left:546px;top:960px;width:500px;font-size:18.5px;line-height:30.5px;color:var(--text)}
.learn-more{left:546px;top:1085px;width:139px;height:46px;font-size:18px;font-weight:600}

/* reasons */
.reasons{position:absolute;left:0;top:1270px;width:1200px;height:490px;background:var(--mist)}
.section-title{position:absolute;left:0;width:1200px;text-align:center;font-weight:800;color:var(--ink);letter-spacing:-0.5px}
.section-sub{position:absolute;left:0;width:1200px;text-align:center;font-size:21px;font-weight:600;color:var(--text)}
.benefit{position:absolute;width:200px;text-align:center}
.benefit svg{display:block;margin:0 auto}
.benefit h3{margin-top:16px;font-size:19px;font-weight:700;color:var(--brand);letter-spacing:-.3px}
.benefit p{margin-top:8px;font-size:13px;line-height:19.5px;color:var(--text)}

/* mission statement */
.statement-title{position:absolute;left:0;top:1870px;width:1200px;text-align:center;font-size:36px;font-weight:800;color:var(--white);letter-spacing:-0.5px}
.pillar{position:absolute;width:360px;color:var(--white)}
.pillar h3{font-size:27px;font-weight:800;letter-spacing:-.4px;margin-top:26px}
.pillar p{font-size:16px;line-height:23px;margin-top:8px}

/* media */
.media{position:absolute;left:0;top:2345px;width:1200px;height:402px;
  background:linear-gradient(120deg,#3a3b40 0%,#2b2b30 50%,#232226 100%)}
.media-title{left:225px;top:2451px;font-size:36px;font-weight:800;color:var(--white);letter-spacing:-.5px}
.media-copy{left:225px;top:2504px;font-size:21px;line-height:29px;color:var(--white)}
.contact-us{left:226px;top:2596px;width:168px;height:44px;font-size:16px;letter-spacing:.5px}

/* reviews */
.reviews-title{top:2853px;font-size:36px;color:var(--brand)}
.review-quote{position:absolute;left:0;top:2918px;width:1200px;height:36px;line-height:36px;text-align:center;font-size:21px;font-weight:600;color:var(--ink)}
.review-quote .mark{color:var(--brand);font-size:30px;line-height:0;font-weight:800;vertical-align:4px;margin:0 10px}
.review-text{position:absolute;left:300px;top:2964px;width:600px;text-align:center;font-size:17.5px;line-height:24px;color:var(--text)}
.review-author{position:absolute;left:0;top:3028px;width:1200px;text-align:center;font-size:18px;color:var(--brand)}

/* contact form */
.contact{position:absolute;left:0;top:3160px;width:1200px;height:462px;background:var(--mist)}
.field{position:absolute;background:var(--field);font-size:15px;color:var(--muted);padding:14px 18px}
.send{left:511px;top:3513px;width:178px;height:46px;font-size:17px}

/* footer */
.site-footer{position:absolute;left:0;top:3622px;width:1200px;height:316px;background:var(--night)}
.footer-brand{left:134px;top:3698px;font-size:28px;color:var(--white)}
.footer-brand .brand-mark{width:52px;height:72px;background:var(--brand-bright)}
.social{position:absolute;width:25px;height:25px;border-radius:50%;border:1.5px solid var(--brand-bright)}
.footer-nav a,.footer-links a,.footer-links span{position:absolute;font-size:14px;color:#d8d8dc;white-space:nowrap}
.footer-nav a{font-weight:700;letter-spacing:.5px}
.footer-links a{text-decoration:underline;font-size:13px}
.footer-links span{font-weight:700;letter-spacing:.5px}
.footer-map{left:798px;top:3696px;width:269px;height:107px;background:linear-gradient(135deg,#dfe6ee,#c9d4e0);border:2px solid #e0b24a}
.footer-rule{left:0;top:3871px;width:1200px;height:1px;background:#45403f}
.copyright{position:absolute;left:0;top:3894px;width:1200px;text-align:center;font-size:14px;color:#9a9597}
</style>
</head>
<body>

<header class="site-header">
  <a class="brand header-brand" href="#"><span class="brand-mark"></span><span><span class="brand-name">HALVERN</span><span class="brand-name">BUILDERS</span></span></a>
  <nav class="main-nav">
    <a class="current" style="left:524px" href="#">Home</a>
    <a style="left:622px" href="#">About</a>
    <a style="left:722px" href="#">Services</a>
    <a style="left:836px" href="#">Contact Us</a>
  </nav>
  <a class="btn investor-login" href="#">Investor Login</a>
</header>

<section class="hero" role="img" aria-label="Photo of a long cable-stayed bridge stretching across deep blue sea under a cloudy sky"></section>
<h1 class="abs hero-title">Halvern Builders</h1>
<p class="abs hero-lede">is an entrepreneurial firm focused on building<br>and growing transformational companies</p>
<a class="btn get-started" href="#">GET STARTED
  <svg width="16" height="16" viewBox="0 0 16 16"><circle cx="8" cy="8" r="8" fill="#fff"/><path d="M6.5 4.5 10 8l-3.5 3.5" stroke="#0b58a6" stroke-width="2" fill="none"/></svg>
</a>
<svg class="round-arrow" style="left:107px;top:364px" viewBox="0 0 52 52"><circle cx="26" cy="26" r="24" fill="none" stroke="#fff" stroke-width="3"/><path d="M30 15 19 26l11 11" fill="none" stroke="#fff" stroke-width="3"/></svg>
<svg class="round-arrow" style="left:1041px;top:364px" viewBox="0 0 52 52"><circle cx="26" cy="26" r="24" fill="none" stroke="#fff" stroke-width="3"/><path d="M22 15l11 11-11 11" fill="none" stroke="#fff" stroke-width="3"/></svg>

<div class="abs mission-visual" role="img" aria-label="Photo of business people reviewing charts and a laptop at a desk"></div>
<h2 class="abs mission-heading">Our mission is to build meaningful businesses that create enduring value by impacting people in a measurable way.</h2>
<p class="abs mission-copy">Lorem Ipsum is simply dummy text of the printing and typesetting industry. Lorem Ipsum has been the industry's standard dummy text ever since the 1500s,</p>
<a class="btn learn-more" href="#">Learn More</a>

<section class="reasons"></section>
<svg class="abs" style="left:500px;top:1269px" width="200" height="80" viewBox="0 0 200 80"><path d="M0 0h200l-86 72q-14 10-28 0z" fill="#fff"/></svg>
<h2 class="section-title" style="top:1384px;font-size:36px">Reason People Work with Us</h2>
<p class="section-sub" style="top:1437px">Benefits of working with us</p>

<div class="benefit" style="left:152px;top:1494px">
  <svg width="70" height="80" viewBox="0 0 70 80" fill="none" stroke="#0b58a6" stroke-width="2.2" stroke-linecap="round">
    <path d="M35 4v7M12 13l5 5M58 13l-5 5M4 34h7M59 34h7"/>
    <path d="M24 58c0-8-10-12-10-24a21 21 0 0 1 42 0c0 12-10 16-10 24z"/>
    <path d="M26 64h18M27 70h16M30 76h10M30 58V38l5 5 5-5v20"/>
  </svg>
  <h3>Investments</h3>
  <p>Lorem Ipsum is simply text of printing and typesetting industry. Lorem Ipsum has Lorem Ipsum</p>
</div>
<div class="benefit" style="left:378px;top:1494px">
  <svg width="70" height="80" viewBox="0 0 70 80" fill="none" stroke="#0b58a6" stroke-width="2.4" stroke-linecap="round" stroke-linejoin="round">
    <circle cx="35" cy="42" r="31"/><path d="M21 43l10 10 19-21"/>
  </svg>
  <h3>Zero Fees</h3>
  <p>Lorem Ipsum is simply text of printing and typesetting industry. Lorem Ipsum has Lorem Ipsum</p>
</div>
<div class="benefit" style="left:612px;top:1494px">
  <svg width="86" height="80" viewBox="0 0 86 80" fill="none" stroke="#0b58a6" stroke-width="2.2" stroke-linejoin="round" stroke-linecap="round">
    <path d="M3 30 18 14l12 10M83 30 68 14l-10 8"/>
    <path d="M30 24 46 18l14 6 14 14-22 24"/>
    <path d="M12 36l18 24c3 4 8 4 11 0"/>
    <path d="M22 48l12 14M28 42l14 16M36 38l14 14M40 24l-8 10c-2 3 2 7 5 5l9-7"/>
  </svg>
  <h3>Stress &amp; Hassle Free</h3>
  <p>Lorem Ipsum is simply text of printing and typesetting industry. Lorem Ipsum has Lorem Ipsum</p>
</div>
<div class="benefit" style="left:848px;top:1494px">
  <svg width="86" height="80" viewBox="0 0 86 80" fill="none" stroke="#0b58a6" stroke-width="2.2" stroke-linejoin="round">
    <path d="M6 30 44 16l36 14-38 16z"/><path d="M6 38l36 16 38-16M6 46l36 16 38-16M6 54l36 16 38-16"/>
    <path d="M22 28l24-8M30 33l24-9"/>
  </svg>
  <h3>Cash Management</h3>
  <p>Lorem Ipsum is simply text of printing and typesetting industry. Lorem Ipsum has Lorem Ipsum</p>
</div>

<svg class="abs" style="left:0;top:1757px" width="1200" height="589" viewBox="0 0 1200 589">
  <path d="M0 90 600 1v588H0z" fill="#0e5aa7"/>
  <path d="M600 1l600 96v492H600z" fill="#0d66b5"/>
</svg>
<h2 class="statement-title">The Mission Statement:</h2>

<div class="pillar" style="left:168px;top:1970px">
  <svg width="104" height="104" viewBox="0 0 104 104" fill="none" stroke="#fff" stroke-width="2.6" stroke-linecap="round" stroke-linejoin="round">
    <path d="M16 8l6 6M8 22h8M88 8l-6 6M96 22h-8"/>
    <path d="M52 100V14M52 14c-10 10-10 24 0 34 10-10 10-24 0-34z"/>
    <path d="M52 66c-6-12-22-18-34-14 4 14 20 18 34 14zM52 66c6-12 22-18 34-14-4 14-20 18-34 14z"/>
    <path d="M52 84c-10-10-30-12-44-6 8 14 30 14 44 6zM52 84c10-10 30-12 44-6-8 14-30 14-44 6z"/>
  </svg>
  <h3>Ground Up</h3>
  <p>Our ground up business applies a proven analytic process to identify value edge, a form of competitive advantage. We architect transformational companies and are deliberate in creating the foundation necessary to lead an industry.</p>
</div>
<div class="pillar" style="left:691px;top:1970px;width:350px">
  <svg width="104" height="104" viewBox="0 0 104 104" fill="none" stroke="#fff" stroke-width="2.6" stroke-linecap="round" stroke-linejoin="round">
    <circle cx="52" cy="34" r="28" stroke-dasharray="6 6"/>
    <rect x="38" y="20" width="28" height="28"/>
    <path d="M52 26l3.5 7 7.5 1-5.5 5 1.5 7.5-7-3.8-7 3.8 1.5-7.5-5.5-5 7.5-1z"/>
    <path d="M8 46v26l16 18v12h12V84L26 70c-3-4 2-8 6-5l6 6"/>
    <path d="M96 46v26L80 90v12H68V84l10-14c3-4-2-8-6-5l-6 6"/>
  </svg>
  <h3>Special Opportunities</h3>
  <p>We partner with exceptional teams that create value by transforming lives. Our investment focus includes large companies and spin-outs.</p>
</div>

<section class="media" role="img" aria-label="Darkened photo of people working over papers and charts at a table"></section>
<h2 class="abs media-title">Halvern Builders</h2>
<p class="abs media-copy">For media inquiries,<br>please contact press@halvernbuilders.com</p>
<a class="btn contact-us" href="#">CONTACT US
  <svg width="16" height="16" viewBox="0 0 16 16"><circle cx="8" cy="8" r="8" fill="#fff"/><path d="M6.5 4.5 10 8l-3.5 3.5" stroke="#0b58a6" stroke-width="2" fill="none"/></svg>
</a>

<h2 class="section-title reviews-title">Reviews</h2>
<p class="review-quote"><span class="mark">&ldquo;</span>Lorem Ipsum is simply dummy text<span class="mark">&rdquo;</span></p>
<p class="review-text">the printing and typesetting industry. Lorem Ipsum has been the industry's standard dummy text ever since the 1500s, when an unknown printer took</p>
<p class="review-author">By Author Name</p>
<svg class="round-arrow" style="left:198px;top:2959px;width:42px;height:42px" viewBox="0 0 52 52"><circle cx="26" cy="26" r="24" fill="none" stroke="#8a8a90" stroke-width="2.5"/><path d="M30 16 20 26l10 10" fill="none" stroke="#8a8a90" stroke-width="2.5"/></svg>
<svg class="round-arrow" style="left:960px;top:2959px;width:42px;height:42px" viewBox="0 0 52 52"><circle cx="26" cy="26" r="24" fill="none" stroke="#8a8a90" stroke-width="2.5"/><path d="M22 16l10 10-10 10" fill="none" stroke="#8a8a90" stroke-width="2.5"/></svg>

<section class="contact"></section>
<h2 class="section-title" style="top:3210px;font-size:39px">Contact Form</h2>
<p class="section-sub" style="top:3260px;color:var(--ink)">Speak with a our Expert today.</p>
<div class="field" style="left:252px;top:3316px;width:226px;height:43px">Full Name</div>
<div class="field" style="left:486px;top:3316px;width:226px;height:43px">Phone</div>
<div class="field" style="left:720px;top:3316px;width:228px;height:43px">Email</div>
<div class="field" style="left:252px;top:3368px;width:696px;height:118px">Message</div>
<a class="btn send" href="#">Send to Us</a>

<footer class="site-footer"></footer>
<a class="brand footer-brand" href="#"><span class="brand-mark"></span><span><span class="brand-name">HALVERN</span><span class="brand-name">BUILDERS</span></span></a>
<span class="social" style="left:134px;top:3801px"></span>
<span class="social" style="left:167px;top:3801px"></span>
<span class="social" style="left:199px;top:3801px"></span>
<span class="social" style="left:233px;top:3801px"></span>
<nav class="footer-nav">
  <a style="left:449px;top:3694px" href="#">HOME</a>
  <a style="left:449px;top:3724px" href="#">ABOUT</a>
  <a style="left:449px;top:3753px" href="#">SERVICES</a>
  <a style="left:449px;top:3784px" href="#">CONTACT US</a>
</nav>
<div class="footer-links">
  <span style="left:625px;top:3692px">CONTACT</span>
  <a style="left:625px;top:3730px" href="#">FAQ</a>
  <a style="left:625px;top:3757px" href="#">Testimonials</a>
  <a style="left:625px;top:3785px" href="#">Contact Us</a>
</div>
<div class="abs footer-map" role="img" aria-label="Small street map showing the office location"></div>
<div class="abs footer-rule"></div>
<p class="copyright">© 2021 Halvern Builders. All Rights are Reserved.</p>

</body>
</html>
```